Natural Handmade Cosmetics Line

I'm looking for a range of labels for a natural handmade Cosmetics company in UK. I'm looking to print the labels on a transparent substrate. The ingredients & Details are on the website. Varenta means Lovely or beloved in latin. The products are designed & manufactured by hand but I want to give the impression of a high end cosmetic brand.

I would like a tag line of some description like "Natural, Pure, Handmade" included

The name of the company is varenta cosmetics (www.varenta.co.uk) and I have the following products (All skin types)

1. Orange & Rose Toner - 150ml (Length: 14cm / hight 9.5cm)
2. Grapefruit Cleanser - 150g (Length 14cm / Hight 9.5cm)
3. Balancing Facial Oil - 30ml (Length 10.5cm / Hight 4.6cm)
4. Frankincense & Neroli Facial Oil - 30ml (Length 10.5cm / Hight 4.6cm)
5. Neroli Moisturizing Face Cream - 50g (Length 15cm / Hight 5cm)
6. Lavender & Neroli Hand Cream - 100g (Length 15cm / Hight 8cm)
7. Tangerine Lip Balm - 4g (Length 5.4cm / Hight 4.6cm) - Lip Balm Tube
8. Mandarin Treatment Balm 50g (Length16.4cm / Hight 3.1cm)
9. Lemon & Tangerine Body Butter - 100g (Length 29cm / Hight 2.5cm)
10. Ylang Ylang & Bergamot Body Butter - 100g (Length 29cm / Hight 2.5cm)

Ideally in the future I would like to get some boxes designed.

I like the following designs

https://www.trumolia.co.uk/face/range/product-family/daily-essentials/
http://www.skyfoxten.co.uk/shop-for-products/natural-skin-care/organic-moisturiser-products
http://www.kuvaderm.com/
http://www.lumaderm.com/
http://www.thebrightmeadowcompany.co.uk/organic-natural-skincare/dry-sensitive/lumaderm-daily-moisture-for-men.html

Dimensions altered

Target Market(s)

Targeting woman of 25+

Industry/Entity Type

Cosmetics

Requirements
Must have
• The correct symbols which are included

```html
<!DOCTYPE html>
<html lang="en">
<head>
<meta charset="utf-8">
<title>Varenta label range</title>
<link rel="stylesheet" href="https://fonts.googleapis.com/css2?family=Bodoni+Moda:wght@600&family=Questrial&family=Fira+Sans+Condensed:wght@400&display=swap">
<style>
  :root {
    --ink: #111111;
    --tagline: #9a9a9a;
    --paper: #ffffff;
    --edge: #d4d4d4;
    --band-text: #ffffff;
    --toner: #f39432;
    --cleanser: #4b1b5b;
    --balancing: #46b04f;
    --neroli-oil: #e9413e;
    --face-cream: #00898a;
    --hand-cream: #b591c1;
  }
  * { margin: 0; padding: 0; box-sizing: border-box; }
  html, body { width: 1200px; height: 954px; overflow: hidden; background: var(--paper); }
  .sheet { position: relative; width: 1200px; height: 954px; }

  .label {
    position: absolute;
    background: var(--paper);
    border: 1px solid var(--edge);
    overflow: hidden;
  }
  .label .line {
    position: absolute;
    left: 0; right: 0;
    text-align: center;
    line-height: 1;
    white-space: nowrap;
  }
  .brand-name {
    font-family: "Bodoni Moda", serif;
    font-weight: 600;
    color: var(--ink);
    letter-spacing: -0.01em;
  }
  .tagline {
    font-family: "Questrial", sans-serif;
    color: var(--tagline);
  }
  .band {
    position: absolute;
    left: 0; right: 0; bottom: 0;
    background: var(--band-colour);
  }
  .band .product,
  .band .detail {
    font-family: "Fira Sans Condensed", sans-serif;
    color: var(--band-text);
  }
  .band .size {
    font-family: "Questrial", sans-serif;
    color: var(--band-text);
  }

  .toner      { --band-colour: var(--toner); }
  .cleanser   { --band-colour: var(--cleanser); }
  .balancing  { --band-colour: var(--balancing); }
  .neroli-oil { --band-colour: var(--neroli-oil); }
  .face-cream { --band-colour: var(--face-cream); }
  .hand-cream { --band-colour: var(--hand-cream); }
</style>
</head>
<body>
<main class="sheet">

  <!-- Orange & Rose Toner -->
  <section class="label toner" style="left:23px;top:16px;width:517px;height:351px;">
    <div class="line brand-name" style="top:110px;font-size:62px;">Varenta</div>
    <div class="line tagline" style="top:185px;font-size:16px;">Natural Handmade skincare</div>
    <div class="band" style="height:127px;" role="img" aria-label="Orange band with a soft swirling leaf pattern">
      <div class="line product" style="top:23px;font-size:15px;">Orange &amp; Rose Toner</div>
      <div class="line size" style="top:46px;font-size:14px;">150mle</div>
    </div>
  </section>

  <!-- Grapefruit Cleanser -->
  <section class="label cleanser" style="left:23px;top:409px;width:517px;height:351px;">
    <div class="line brand-name" style="top:110px;font-size:62px;">Varenta</div>
    <div class="line tagline" style="top:170px;font-size:16px;">Natural Handmade skincare</div>
    <div class="band" style="height:127px;" role="img" aria-label="Deep purple band with a soft swirling leaf pattern">
      <div class="line product" style="top:15px;font-size:15px;">Grapefruit Cleanser</div>
      <div class="line size" style="top:38px;font-size:14px;">150mle</div>
    </div>
  </section>

  <!-- Balancing Facial Oil -->
  <section class="label balancing" style="left:602px;top:12px;width:388px;height:171px;">
    <div class="line brand-name" style="top:61px;font-size:29px;">Varenta</div>
    <div class="line tagline" style="top:90px;font-size:7.5px;">Natural Handmade skincare</div>
    <div class="band" style="height:51px;" role="img" aria-label="Green band with a soft swirling leaf pattern">
      <div class="line product" style="top:6px;font-size:8px;">Balancing facial Oil</div>
      <div class="line detail" style="top:17px;font-size:6px;">All Skin Tipes</div>
      <div class="line size" style="top:26px;font-size:6px;">30mle</div>
    </div>
  </section>

  <!-- Neroli & Frankincense Facial Oil -->
  <section class="label neroli-oil" style="left:602px;top:202px;width:388px;height:170px;">
    <div class="line brand-name" style="top:63px;font-size:29px;">Varenta</div>
    <div class="line tagline" style="top:91px;font-size:7.5px;">Natural Handmade skincare</div>
    <div class="band" style="height:51px;" role="img" aria-label="Red band with a soft swirling leaf pattern">
      <div class="line product" style="top:4px;font-size:7px;">Neroli &amp; Frankincense</div>
      <div class="line product" style="top:12px;font-size:7px;">Facial Oil</div>
      <div class="line detail" style="top:23px;font-size:5.5px;">All Skin Tipes</div>
      <div class="line size" style="top:31px;font-size:5.5px;">30mle</div>
    </div>
  </section>

  <!-- Neroli Moisture Facial Cream -->
  <section class="label face-cream" style="left:603px;top:390px;width:553px;height:185px;">
    <div class="line brand-name" style="top:56px;font-size:34px;">Varenta</div>
    <div class="line tagline" style="top:91px;font-size:9px;">Natural Handmade skincare</div>
    <div class="band" style="height:63px;" role="img" aria-label="Teal band with a soft swirling leaf pattern">
      <div class="line product" style="top:8px;font-size:8px;">Neroli Moisture Facial Cream</div>
      <div class="line detail" style="top:20px;font-size:7px;">All Skin Tipes</div>
      <div class="line size" style="top:40px;font-size:7px;">15mle</div>
    </div>
  </section>

  <!-- Lavender & Neroli Hand Cream -->
  <section class="label hand-cream" style="left:605px;top:601px;width:554px;height:296px;">
    <div class="line brand-name" style="top:95px;font-size:56px;">Varenta</div>
    <div class="line tagline" style="top:156px;font-size:14px;">Natural Handmade skincare</div>
    <div class="band" style="height:98px;" role="img" aria-label="Lilac band with a soft swirling leaf pattern">
      <div class="line product" style="top:8px;font-size:14px;">Lavender &amp; Neroli</div>
      <div class="line product" style="top:26px;font-size:14px;">Hand&nbsp; Cream</div>
      <div class="line detail" style="top:46px;font-size:7.5px;">All Skin Tipes</div>
      <div class="line size" style="top:67px;font-size:13px;">150mle</div>
    </div>
  </section>

</main>
</body>
</html>
```